Free Offer Book Cover

I am creating a funnel page where I offer a free download of a PDF called. First Season Field Kit. A compass for fresh captains. I have included samples of other book covers. It can look like a book, or a checklist, or something that illustrates what they are getting. Bright Harbor Coaching is the company if you could get the logo into the book cover as well.

Target Market(s)

New leaders, young professionals

Font styles to use
Sans Serif

Requirements
Must have
• Name of content. First Season Field Kit for fresh captains.

```html
<!DOCTYPE html>
<html lang="en">
<head>
<meta charset="utf-8">
<title>Bright Harbor Coaching – First Season Field Kit</title>
<link href="https://fonts.googleapis.com/css2?family=Nunito:wght@400;600&family=Oswald:wght@400;600;700&family=Roboto+Condensed:wght@300;400&family=Open+Sans:wght@400;700&display=swap" rel="stylesheet">
<style>
  :root {
    --page-bg: #2e2e2e;
    --accent: #e8402f;
    --accent-soft: #e04a4a;
    --cover-red: #ee3a48;
    --white: #ffffff;
    --field-bg: #f4f4f4;
    --field-text: #7a7a7a;
    --tag-bg: #4a4a4a;
    --cover-dark: #0e0e0e;
    --cover-mid: #2a2a2a;
  }
  * { box-sizing: border-box; margin: 0; padding: 0; }
  html, body { width: 1200px; height: 754px; overflow: hidden; background: var(--page-bg); }
  .page { position: relative; width: 1200px; height: 754px; }

  .cover-frame {
    position: absolute; left: 21px; top: 19px; width: 555px; height: 713px;
    border: 2px solid var(--accent-soft);
  }
  .book-cover {
    position: absolute; left: 118px; top: 150px; width: 318px; height: 420px;
    background: linear-gradient(135deg, var(--cover-mid) 0%, var(--cover-dark) 70%);
    box-shadow: 0 18px 40px rgba(0,0,0,.55);
    border-left: 10px solid #111;
    font-family: 'Oswald', sans-serif; text-align: center;
    padding: 40px 22px 0;
  }
  .cover-kicker { display: flex; align-items: center; justify-content: center; gap: 14px; color: var(--cover-red); font-weight: 700; font-size: 34px; line-height: 1; }
  .cover-kicker::before, .cover-kicker::after { content: ""; width: 40px; height: 6px; background: var(--cover-red); }
  .cover-title { color: var(--cover-red); font-weight: 700; font-size: 64px; line-height: 1; margin-top: 10px; }
  .cover-subtitle { color: #e6e6e6; font-weight: 600; font-size: 46px; line-height: 1; margin-top: 6px; }
  .cover-brand { color: var(--cover-red); font-family: 'Roboto Condensed', sans-serif; font-weight: 400; font-size: 17px; margin-top: 30px; letter-spacing: .5px; }
  .cover-rule { height: 6px; background: var(--cover-red); margin: 26px 0 12px; }
  .cover-tagline { color: var(--cover-red); font-size: 17px; font-weight: 600; letter-spacing: .5px; text-transform: uppercase; }

  .offer { position: absolute; left: 600px; top: 0; width: 580px; text-align: center; }
  .brand-mark { display: flex; align-items: center; justify-content: center; gap: 10px; margin-top: 78px; height: 40px; font-family: 'Roboto Condensed', sans-serif; font-size: 26px; font-weight: 400; color: var(--accent); }
  .brand-dot { width: 16px; height: 16px; border-radius: 50%; background: var(--accent); }
  .headline { font-family: 'Nunito', sans-serif; color: var(--accent); font-size: 74px; font-weight: 400; line-height: 1; margin-top: 78px; }
  .subhead { font-family: 'Nunito', sans-serif; color: var(--white); font-size: 35px; font-weight: 400; line-height: 1.08; margin-top: 6px; }
  .offer-lines { font-family: 'Roboto Condensed', sans-serif; color: var(--accent); font-weight: 300; font-size: 27px; line-height: 1.5; margin-top: 6px; }

  .signup { position: absolute; left: 615px; top: 468px; width: 553px; }
  .field { position: relative; height: 52px; background: var(--field-bg); border-radius: 3px; margin-bottom: 22px; padding: 0 18px; display: flex; align-items: center; font-family: 'Open Sans', sans-serif; font-size: 15px; color: var(--field-text); box-shadow: 0 2px 3px rgba(0,0,0,.35); }
  .tag { position: absolute; left: 12px; bottom: -6px; background: var(--tag-bg); color: #eee; font-family: 'Open Sans', sans-serif; font-weight: 700; font-size: 7px; padding: 2px 5px; text-transform: uppercase; }
  .submit { position: relative; height: 82px; background: var(--accent); border-radius: 2px; display: flex; align-items: center; justify-content: center; font-family: 'Oswald', sans-serif; font-size: 37px; color: var(--white); box-shadow: 0 3px 4px rgba(0,0,0,.4); margin-top: 10px; }
</style>
</head>
<body>
<main class="page">
  <section class="cover-frame">
    <div class="book-cover">
      <div class="cover-kicker">First</div>
      <div class="cover-title">SEASON</div>
      <div class="cover-subtitle">FIELD KIT</div>
      <div class="cover-brand">Bright Harbor Coaching</div>
      <div class="cover-rule"></div>
      <div class="cover-tagline">A compass for fresh captains</div>
    </div>
  </section>

  <section class="offer">
    <div class="brand-mark"><span class="brand-dot"></span>Bright Harbor Coaching</div>
    <h1 class="headline">DISCOVER</h1>
    <p class="subhead">What you need to do NOW to<br>become a Bright Harbor Leader!</p>
    <p class="offer-lines">Get your free First Season Field Kit.<br>The Compass for Fresh Captains.</p>
  </section>

  <form class="signup">
    <div class="field">Enter Your Name Here...<span class="tag">Name</span></div>
    <div class="field">Enter Your Email Address Here...<span class="tag">Email</span></div>
    <div class="submit">Click to Get Your Field Kit<span class="tag">Submits the page</span></div>
  </form>
</main>
</body>
</html>
```